New Print Material Needed for Renovation Company

We are looking to update our current Print Material to reflect the current process we offer to our clients. A lot of the information is also outdated along with many of the photos that are currently being used. We are a renovation company that specializes in residential and commercial renovations and custom builds.This project is MULTIPLE pages. We will pay the chosen designer an extra fee for the designing 3-4 additional pages that are similar to the chosen design. Attached is our current Print Material. We are hoping to update the look of them and some of the messaging. Our current company colors are white, blue and light grey and it will remain that way.

Industry/Entity Type

Construction Company

Font styles to use
Sans Serif

Colors
3176b5
ffffff

Requirements
Must have
• Easy to explain the process
• Easy to read and understand let alone
• Easy to navigate
Nice to have
• As much creativity as possible
Should not have
• no confusing text
• no confusing layout

```html
<!DOCTYPE html>
<html lang="en">
<head>
<meta charset="utf-8">
<title>Master Builder Timeline – Harbourline General Contractors</title>
<link href="https://fonts.googleapis.com/css2?family=Montserrat:wght@300;400;500;700;800&display=swap" rel="stylesheet">
<style>
  :root{
    --backdrop:#37485a;
    --paper:#ffffff;
    --brand-blue:#0047ff;
    --soft-grey:#a6a6a6;
    --panel-blue:#dcf0fa;
    --panel-pale:#eef8fd;
    --body-grey:#7a7a7a;
    --rule-grey:#9a9a9a;
  }
  *{box-sizing:border-box;margin:0;padding:0}
  html,body{width:848px;height:1200px;overflow:hidden;background:var(--backdrop)}
  body{position:relative;font-family:'Montserrat',sans-serif}

  .sheet{position:absolute;left:34px;top:49px;width:780px;height:1102px;background:var(--paper);
    box-shadow:6px 8px 14px rgba(0,0,0,.45);overflow:hidden}
  .sheet-top-band{position:absolute;left:0;top:0;width:100%;height:22px;background:var(--soft-grey)}
  .sheet-bottom-band{position:absolute;left:0;bottom:0;width:100%;height:37px;background:var(--brand-blue)}

  .brand-tab{position:absolute;left:244px;top:0;width:290px;height:85px}
  .brand-mark{position:absolute;left:69px;top:14px;width:54px;height:54px;border:5px solid var(--paper);border-radius:50%}
  .brand-name{position:absolute;left:134px;top:15px;color:var(--paper);font-weight:500;font-size:16px;line-height:17px}

  .title-icon{position:absolute;left:48px;top:118px;width:90px;height:88px;border-radius:50%;
    background:radial-gradient(circle,#e3ebff 0 45%,#c7d6ff 46% 100%)}
  .page-title{position:absolute;left:156px;top:140px;width:580px;height:60px}
  .page-title text{font-family:'Montserrat',sans-serif;font-weight:800;font-size:46px;fill:var(--brand-blue)}

  .lane{position:absolute;top:302px;height:745px}
  .lane-design{left:17px;width:248px;background:var(--panel-blue)}
  .lane-plan{left:274px;width:230px;background:var(--panel-pale)}
  .lane-build{left:512px;width:248px;background:var(--panel-blue)}

  .phase{position:absolute;top:277px;width:194px;height:289px;border-radius:14px;background:var(--paper);
    box-shadow:0 2px 8px rgba(0,40,160,.35)}
  .phase-cap{position:absolute;left:0;top:0;width:100%;height:29px;background:var(--soft-grey);border-radius:14px 14px 0 0}
  .phase-art{position:absolute;left:42px;top:80px;width:110px;height:112px;border-radius:10px;
    background:linear-gradient(135deg,#2f6bff,#0047ff)}
  .phase-label{position:absolute;left:0;bottom:0;width:100%;height:55px;background:var(--brand-blue);
    border-radius:0 0 14px 14px;color:var(--paper);font-weight:300;font-size:38px;letter-spacing:1px;
    text-align:center;line-height:55px}
  .phase-label::after{content:"";position:absolute;left:50%;bottom:-17px;margin-left:-17px;
    border-left:17px solid transparent;border-right:17px solid transparent;border-top:17px solid var(--brand-blue)}
  .phase .hex{left:64px;top:-22px}
  .phase .hex span{font-size:34px;font-weight:700}

  .hex{position:absolute;width:66px;height:76px;filter:drop-shadow(0 2px 4px rgba(0,30,140,.45))}
  .hex svg{position:absolute;left:0;top:0;width:100%;height:100%}
  .hex span{position:absolute;left:0;top:0;width:100%;height:100%;display:flex;align-items:center;justify-content:center;
    color:var(--brand-blue);font-weight:800;font-size:29px}

  .step{position:absolute;width:183px;height:124px;background:var(--paper);border-radius:0 0 9px 9px;
    box-shadow:0 2px 6px rgba(0,30,120,.35)}
  .step-head{position:absolute;left:0;top:0;width:100%;height:47px;background:var(--brand-blue);padding:6px 0 0 59px}
  .step-head h3{color:var(--paper);font-weight:800;font-size:13.3px;line-height:16.5px;letter-spacing:.3px}
  .step-text{position:absolute;left:6px;top:64px;width:176px;color:var(--body-grey);font-size:8.4px;line-height:11px;white-space:nowrap}
  .step-rule{position:absolute;left:5px;right:5px;top:105px;height:1px;background:var(--rule-grey)}
  .step-time{position:absolute;left:0;top:110px;width:100%;text-align:center;color:var(--brand-blue);font-weight:700;font-size:8.4px}
  .step .hex{left:-16px;top:-11px}

  .col-1{left:86px}.col-2{left:332px}.col-3{left:579px}
  .row-1{top:659px}.row-2{top:806px}.row-3{top:954px}
  .phase.col-1{left:78px}.phase.col-2{left:325px}.phase.col-3{left:572px}
</style>
</head>
<body>
<svg width="0" height="0" style="position:absolute">
  <defs>
    <polygon id="hex-shape" points="33,3 62,20 62,56 33,73 4,56 4,20" fill="#ffffff" stroke="#0047ff" stroke-width="4" stroke-linejoin="round"/>
  </defs>
</svg>

<main class="sheet">
  <div class="sheet-top-band"></div>

  <header class="brand-tab">
    <svg width="290" height="85" viewBox="0 0 290 85" style="position:absolute;left:0;top:0">
      <path d="M2 0 H288 L272 74 Q270 85 259 85 H31 Q20 85 18 74 Z" fill="#0047ff"/>
    </svg>
    <div class="brand-mark"></div>
    <div class="brand-name">Harbourline<br>General<br>Contractors</div>
  </header>

  <div class="title-icon" role="img" aria-label="Gear with circular arrows icon"></div>
  <h1 class="page-title">
    <svg width="580" height="60" viewBox="0 0 580 60"><text x="0" y="50" textLength="576" lengthAdjust="spacingAndGlyphs">MASTER BUILDER TIMELINE</text></svg>
  </h1>

  <div class="lane lane-design"></div>
  <div class="lane lane-plan"></div>
  <div class="lane lane-build"></div>

  <section class="phase col-1" style="position:absolute;top:277px">
    <div class="phase-cap"></div>
    <div class="hex"><svg viewBox="0 0 66 76"><use href="#hex-shape"/></svg><span>1</span></div>
    <div class="phase-art" role="img" aria-label="Ruler and pencil design icon"></div>
    <div class="phase-label">DESIGN</div>
  </section>
  <section class="phase col-2">
    <div class="phase-cap"></div>
    <div class="hex"><svg viewBox="0 0 66 76"><use href="#hex-shape"/></svg><span>2</span></div>
    <div class="phase-art" role="img" aria-label="Builder holding blueprint plans icon"></div>
    <div class="phase-label">PLAN</div>
  </section>
  <section class="phase col-3">
    <div class="phase-cap"></div>
    <div class="hex"><svg viewBox="0 0 66 76"><use href="#hex-shape"/></svg><span>3</span></div>
    <div class="phase-art" role="img" aria-label="Crossed wrench and screwdriver icon"></div>
    <div class="phase-label">BUILD</div>
  </section>
</main>

<!-- steps positioned on the page -->
<div style="position:absolute;left:34px;top:49px;width:780px;height:1102px">
  <article class="step col-1 row-1" style="margin-top:-49px;margin-left:-34px">
  </article>
</div>

<div style="position:absolute;left:0;top:0;width:848px;height:1200px">
  <article class="step col-1 row-1">
    <div class="step-head"><h3>INITIAL DESIGN<br>MEETING</h3></div>
    <p class="step-text">Lorem ipsum dolor sit amet, elit, sed<br>diam nonummy nibh tinciduntlaoreet<br>dolore magna aliquam erat volutpat.</p>
    <div class="step-rule"></div><div class="step-time">1-2 WEEKS</div>
    <div class="hex"><svg viewBox="0 0 66 76"><use href="#hex-shape"/></svg><span>01</span></div>
  </article>
  <article class="step col-1 row-2">
    <div class="step-head"><h3>SECOND DESIGN<br>MEETING</h3></div>
    <p class="step-text">Lorem ipsum dolor sit amet, elit, sed<br>diam nonummy nibh tinciduntlaoreet<br>dolore magna aliquam erat volutpat.</p>
    <div class="step-rule"></div><div class="step-time">1-2 WEEKS</div>
    <div class="hex"><svg viewBox="0 0 66 76"><use href="#hex-shape"/></svg><span>02</span></div>
  </article>
  <article class="step col-1 row-3">
    <div class="step-head"><h3>FINAL DESIGN<br>MEETING</h3></div>
    <p class="step-text">Lorem ipsum dolor sit amet, elit, sed<br>diam nonummy nibh tinciduntlaoreet<br>dolore magna aliquam erat volutpat.</p>
    <div class="step-rule"></div><div class="step-time">1-3 WEEKS</div>
    <div class="hex"><svg viewBox="0 0 66 76"><use href="#hex-shape"/></svg><span>03</span></div>
  </article>

  <article class="step col-2 row-1">
    <div class="step-head"><h3>MATERIAL<br>SELECTION</h3></div>
    <p class="step-text">Lorem ipsum dolor sit amet, elit, sed<br>diam nonummy nibh tinciduntlaoreet<br>dolore magna aliquam erat volutpat.</p>
    <div class="step-rule"></div><div class="step-time">1-4 WEEKS</div>
    <div class="hex"><svg viewBox="0 0 66 76"><use href="#hex-shape"/></svg><span>04</span></div>
  </article>
  <article class="step col-2 row-2">
    <div class="step-head"><h3>ENGINEER<br>DRAWINGS</h3></div>
    <p class="step-text">Lorem ipsum dolor sit amet, elit, sed<br>diam nonummy nibh tinciduntlaoreet<br>dolore magna aliquam erat volutpat.</p>
    <div class="step-rule"></div><div class="step-time">2-4 WEEKS</div>
    <div class="hex"><svg viewBox="0 0 66 76"><use href="#hex-shape"/></svg><span>05</span></div>
  </article>
  <article class="step col-2 row-3">
    <div class="step-head"><h3>BUILDING<br>PERMIT PLANS</h3></div>
    <p class="step-text">Lorem ipsum dolor sit amet, elit, sed<br>diam nonummy nibh tinciduntlaoreet<br>dolore magna aliquam erat volutpat.</p>
    <div class="step-rule"></div><div class="step-time">3-25 WEEKS</div>
    <div class="hex"><svg viewBox="0 0 66 76"><use href="#hex-shape"/></svg><span>06</span></div>
  </article>

  <article class="step col-3 row-1">
    <div class="step-head"><h3>MATERIAL<br>FINALIZATION</h3></div>
    <p class="step-text">Lorem ipsum dolor sit amet, elit, sed<br>diam nonummy nibh tinciduntlaoreet<br>dolore magna aliquam erat volutpat.</p>
    <div class="step-rule"></div><div class="step-time">2-4 WEEKS</div>
    <div class="hex"><svg viewBox="0 0 66 76"><use href="#hex-shape"/></svg><span>07</span></div>
  </article>
  <article class="step col-3 row-2">
    <div class="step-head"><h3>CONSTRUCTION<br>PLANS</h3></div>
    <p class="step-text">Lorem ipsum dolor sit amet, elit, sed<br>diam nonummy nibh tinciduntlaoreet<br>dolore magna aliquam erat volutpat.</p>
    <div class="step-rule"></div><div class="step-time">2-6 WEEKS</div>
    <div class="hex"><svg viewBox="0 0 66 76"><use href="#hex-shape"/></svg><span>08</span></div>
  </article>
  <article class="step col-3 row-3">
    <div class="step-head"><h3>SCHEDULING</h3></div>
    <p class="step-text">Lorem ipsum dolor sit amet, elit, sed<br>diam nonummy nibh tinciduntlaoreet<br>dolore magna aliquam erat volutpat.</p>
    <div class="step-rule"></div><div class="step-time">2-4 WEEKS</div>
    <div class="hex"><svg viewBox="0 0 66 76"><use href="#hex-shape"/></svg><span>09</span></div>
  </article>
</div>

<div style="position:absolute;left:34px;top:1114px;width:780px;height:37px;background:var(--brand-blue)"></div>
</body>
</html>
```